Plumbing and heating business card design

i need a new business card for the company i work for called Dr. Brightwell. It is a plumbing and heating company that has been operating for over 30 years. We are not like these big plumbing companies that have ways to charge the customer as much as possible. Our company does only what is necessary and what is needed to do the job right the first time without the high cost. we are a neighborhood business which kind of explains why we don't charge customers through the roof. I would like to see a design with a nice background anything but just plain white. maybe like a light blue at the top of the design. on the back of the card i would like it to say " T. Vantelli's Dr. Brightwell". maybe add some color to the lettering on the front of the card for example blue font for plumbing and red font for heating. raised print. im sure Cardmerro designers will make it look good. The final design should help spread a good word about our company and help grow business.

Industry/Entity Type

Business

Contact Information for Business Card

Dr. Brightwell, Plumbing & heating, Daniel Hosker, Northeast District Operations manager, 4827 Pellworth st., Office:(555)-782-1093, doctorbrightwell@pipemailer.example

Requirements
Must have
• raised print finish and a nice sturdy feel.

```html
<!DOCTYPE html>
<html lang="en">
<head>
<meta charset="utf-8">
<title>Dr. Brightwell – Business Card</title>
<link href="https://fonts.googleapis.com/css2?family=Ubuntu:wght@300;500;700&family=Oswald:wght@600&display=swap" rel="stylesheet">
<style>
  :root {
    --bg: #eef0f2;
    --card-blue: #2b97e2;
    --brand-blue: #2b8fdc;
    --accent-orange: #f07a1a;
    --white: #ffffff;
    --shadow: rgba(0, 0, 0, 0.18);
  }
  * { margin: 0; padding: 0; box-sizing: border-box; }
  html, body {
    width: 1010px;
    height: 1200px;
    overflow: hidden;
    background: var(--bg);
    font-family: "Ubuntu", sans-serif;
  }
  .canvas { position: relative; width: 1010px; height: 1200px; }
  .card {
    position: absolute;
    width: 800px;
    height: 461px;
    border-radius: 28px;
    overflow: hidden;
    box-shadow: 0 3px 8px var(--shadow);
  }
  .card-front { left: 97px; top: 92px; background: var(--white); }
  .card-back { left: 107px; top: 650px; background: var(--card-blue); }
  .front-art { position: absolute; inset: 0; }
  .brand {
    position: absolute;
    left: 0; right: 0; top: 60px;
    display: flex;
    justify-content: center;
    align-items: center;
    gap: 14px;
  }
  .brand-dot {
    width: 34px; height: 34px;
    border-radius: 50%;
    background: var(--accent-orange);
  }
  .brand-name {
    font-weight: 700;
    font-size: 40px;
    color: var(--brand-blue);
    letter-spacing: 0.5px;
  }
  .person {
    position: absolute;
    right: 439px;
    top: 306px;
    text-align: right;
    color: var(--white);
  }
  .person-name { font-weight: 700; font-size: 27px; line-height: 34px; }
  .person-role { font-weight: 300; font-size: 21px; line-height: 27px; letter-spacing: 0.5px; }
  .divider {
    position: absolute;
    left: 397px; top: 282px;
    width: 3px; height: 141px;
    background: var(--white);
  }
  .contacts {
    position: absolute;
    left: 412px; top: 306px;
    list-style: none;
    color: var(--white);
  }
  .contacts li {
    display: flex;
    align-items: center;
    height: 32px;
    font-weight: 700;
    font-size: 22px;
    letter-spacing: 0.3px;
  }
  .contacts li.contact-email { font-size: 17px; }
  .contacts svg { width: 24px; height: 22px; margin-right: 20px; flex: none; fill: var(--white); }
  .back-title {
    position: absolute;
    left: 0; right: 0; top: 198px;
    text-align: center;
    font-family: "Oswald", sans-serif;
    font-weight: 600;
    font-size: 56px;
    color: var(--white);
    letter-spacing: 1px;
    text-shadow: 1px 1px 0 #c9d6e2, 2px 3px 3px rgba(0,0,0,0.35);
  }
</style>
</head>
<body>
<main class="canvas">
  <section class="card card-front">
    <svg class="front-art" viewBox="0 0 800 461" width="800" height="461" aria-hidden="true">
      <path d="M0 133 Q400 373 800 113 L800 461 L0 461 Z" fill="var(--card-blue)"/>
      <path d="M0 133 Q400 373 800 113" fill="none" stroke="var(--accent-orange)" stroke-width="6"/>
    </svg>
    <div class="brand">
      <span class="brand-dot"></span>
      <span class="brand-name">Dr. Brightwell</span>
    </div>
    <div class="person">
      <p class="person-name">Daniel Hosker</p>
      <p class="person-role">Northeast District</p>
      <p class="person-role">Operations manager</p>
    </div>
    <div class="divider"></div>
    <ul class="contacts">
      <li class="contact-phone">
        <svg viewBox="0 0 24 24"><path d="M6.6 2.5l3 3.2-1.8 2.4c1.3 2.9 3.3 5 6.2 6.3l2.3-1.8 3.2 3-2.2 3.4C10 18.6 4.9 13.4 3.2 5.2z"/></svg>
        (555)-782-1093
      </li>
      <li class="contact-email">
        <svg viewBox="0 0 24 22"><path d="M2 3h20v16H2z M4 5v1l8 6 8-6V5z M4 8.5V17h16V8.5l-8 6z" fill-rule="evenodd"/></svg>
        doctorbrightwell@pipemailer.example
      </li>
      <li class="contact-address">
        <svg viewBox="0 0 24 22"><path d="M12 2L1 11h3v10h16V11h3z M10 14h4v7h-4z" fill-rule="evenodd"/></svg>
        4827 Pellworth st.
      </li>
    </ul>
  </section>

  <section class="card card-back">
    <h1 class="back-title">T. Vantelli's Dr. Brightwell</h1>
  </section>
</main>
</body>
</html>
```